Brisk Hive 360 Postcard Design, Double-Sided

Please read carefully and see attached. Designers that do not follow these instructions will not be selected. Limit ONE design submission per artist. The ONE design submission shall show both the front and the back designs. Designs must comply with the attached dismensions accounting for the bleed area to prevent designs from being cut off during printing. The attached business card and door tag designs have already been created, printed and are in use. The postcard shall be similar in design to the attached business card and door tag. All of the information that you need is attached. The overall size is 4.12" x 6.12" for the front. The back is different, see attached and scale to match template. I would like the Veteran Owned Business logo added as well. It would also be nice to see my photo incorporated somehow. I like the yellow on the door tag. It helps build contrast and pops out. Again, one design submission per designer that shows both the front and the back.

Target Market(s)

Please read all instructions and see attached.

Industry/Entity Type

Requirements
Must have
• Please read all instructions and see attached.
Nice to have
Should not have

```html
<!DOCTYPE html>
<html lang="en">
<head>
<meta charset="utf-8">
<title>Brisk Hive 360 Postcard – Front and Back</title>
<link href="https://fonts.googleapis.com/css2?family=Roboto:ital,wght@0,400;0,500;0,700;0,900;1,900&display=swap" rel="stylesheet">
<style>
  :root{
    --stage:#d3d3d3;
    --label:#777777;
    --ink:#1c1c1c;
    --black:#1a1a1a;
    --yellow:#f6ec00;
    --white:#ffffff;
    --red:#e30613;
    --guide:#2bb35a;
    --badge-blue:#27327a;
    --badge-red:#d8262f;
  }
  *{box-sizing:border-box;margin:0;padding:0}
  html,body{width:1200px;height:1200px;overflow:hidden;background:var(--stage);font-family:"Roboto",Arial,sans-serif;color:var(--ink)}
  .side-label{position:absolute;left:0;width:1170px;text-align:center;font-size:23px;color:var(--label)}
  .card{position:absolute;left:262px;width:676px;height:455px;background:var(--white);overflow:hidden;box-shadow:0 1px 2px rgba(0,0,0,.15)}
  .card-front{top:110px}
  .card-back{top:635px}
  .card svg.art{position:absolute;inset:0}
  .abs{position:absolute}

  /* front */
  .web-tag{left:24px;top:20px;color:var(--white);font-size:13.5px;display:flex;align-items:center;gap:6px}
  .owner-name{left:232px;top:22px;color:var(--white);font-weight:700;font-size:14px;letter-spacing:.2px}
  .owner-role{left:232px;top:37px;color:var(--white);font-size:9.5px}
  .brand-title{left:232px;top:46px;color:var(--yellow);font-weight:900;font-style:italic;font-size:37px;letter-spacing:-1px;white-space:nowrap}
  .brand-rule{left:234px;top:89px;width:256px;height:3px;background:var(--yellow)}
  .brand-sub{left:297px;top:93px;color:var(--yellow);font-weight:900;font-style:italic;font-size:22px}
  .owner-photo{left:14px;top:58px;width:292px;height:352px;border-radius:140px 140px 0 0;background:linear-gradient(180deg,#b98c72 0%,#c9a08a 25%,#c9ccd2 45%,#b8bcc4 100%)}
  .vet-badge{left:30px;top:128px;width:90px;height:90px;border-radius:50%;background:var(--badge-blue);border:6px solid var(--badge-red)}
  .list-block h3{font-size:17.5px;font-weight:700;letter-spacing:.3px;line-height:1}
  .list-block small{display:block;font-size:8.5px;margin:3px 0 4px}
  .list-block ul{list-style:none;font-size:12px;line-height:16px}
  .list-block li{padding-left:11px;position:relative}
  .list-block li::before{content:"";position:absolute;left:0;top:5px;border-left:5px solid var(--yellow);border-top:3px solid transparent;border-bottom:3px solid transparent}
  .benefits{left:356px;top:196px}
  .services{left:493px;top:178px}
  .services h3{margin-bottom:5px}
  .list-divider{left:483px;top:170px;width:1px;height:145px;background:var(--yellow)}
  .front-mark{left:278px;top:340px;width:110px;display:flex;flex-direction:column;align-items:center;gap:4px;color:var(--white);font-weight:700;font-size:13px}
  .front-mark span.dot{width:30px;height:30px;border-radius:50%;border:2px solid var(--white)}

  /* back */
  .back-mark{left:62px;top:66px;width:90px;display:flex;flex-direction:column;align-items:center;gap:4px;font-weight:700;font-size:12px;text-align:center}
  .back-mark span.dot{width:36px;height:36px;border-radius:50%;border:3px solid var(--ink)}
  .vet-badge-back{left:168px;top:60px;width:84px;height:84px;border-radius:50%;background:var(--badge-blue);border:6px solid var(--badge-red)}
  .inquire{left:56px;top:170px;font-weight:700;font-size:19px;white-space:nowrap}
  .inquire b{color:var(--red);font-size:38px;font-weight:700;letter-spacing:.5px}
  .contact-list{left:56px;top:212px;list-style:none}
  .contact-list li{display:flex;align-items:center;gap:12px;height:27px;font-size:16px}
  .contact-list li.phone{font-size:26px;font-weight:700;height:34px;margin-bottom:-2px}
  .contact-list svg{flex:none}
  .stamp-box{left:553px;top:23px;width:100px;height:100px;border:1px solid var(--ink)}
  .address-line{left:415px;width:238px;height:1px;background:#333}
</style>
</head>
<body>

<div class="side-label" style="top:62px">Front Side</div>

<section class="card card-front">
  <svg class="art" width="676" height="455" viewBox="0 0 676 455">
    <polygon points="0,0 676,0 676,52 332,160 0,58" fill="var(--black)"/>
    <polygon points="0,58 332,160 676,52 676,58 332,180 0,66" fill="var(--yellow)"/>
    <polygon points="0,66 332,180 676,58 676,66 332,190 0,70" fill="var(--white)"/>
    <polygon points="0,70 332,190 676,66 676,68 332,193 0,72" fill="var(--yellow)"/>
    <polygon points="0,422 338,298 676,420 676,455 0,455" fill="var(--black)"/>
    <polygon points="0,412 338,296 676,414 676,420 338,316 0,422" fill="var(--yellow)"/>
    <rect x="14" y="14" width="648" height="427" fill="none" stroke="var(--guide)" stroke-width="1" stroke-dasharray="3 2"/>
  </svg>

  <div class="abs owner-photo" role="img" aria-label="Portrait photo of the owner in a light grey work shirt"></div>
  <div class="abs vet-badge" role="img" aria-label="Veteran owned business membership badge"></div>

  <div class="abs web-tag">
    <svg width="14" height="14" viewBox="0 0 14 14"><circle cx="7" cy="7" r="6" fill="none" stroke="var(--yellow)" stroke-width="1.4"/><ellipse cx="7" cy="7" rx="2.6" ry="6" fill="none" stroke="var(--yellow)" stroke-width="1.2"/><line x1="1" y1="7" x2="13" y2="7" stroke="var(--yellow)" stroke-width="1.2"/></svg>
    briskhive360.com
  </div>
  <div class="abs owner-name">DANA R. WHITLOW</div>
  <div class="abs owner-role">OWNER &amp; HANDYMAN</div>
  <div class="abs brand-title">BRISK HIVE 360</div>
  <div class="abs brand-rule"></div>
  <div class="abs brand-sub">HANDYMAN</div>

  <div class="abs list-block benefits">
    <h3>BENEFITS</h3>
    <small>OF USING OUR SERVICES</small>
    <ul><li>Fast Response</li><li>High Quality</li><li>Fair Pricing</li><li>Veteran Owned</li></ul>
  </div>
  <div class="abs list-divider"></div>
  <div class="abs list-block services">
    <h3>SERVICES</h3>
    <ul><li>Assembly</li><li>Small Repairs</li><li>Wifi / Router Setup</li><li>Fabrication</li><li>Hanging Items</li><li>Wireless Device Setup</li><li>Odd Jobs</li></ul>
  </div>

  <div class="abs front-mark"><span class="dot"></span>Brisk Hive 360</div>
</section>

<div class="side-label" style="top:598px">Back Side</div>

<section class="card card-back">
  <svg class="art" width="676" height="455" viewBox="0 0 676 455">
    <polygon points="0,0 195,0 0,66" fill="var(--black)"/>
    <polygon points="150,0 195,0 0,66 0,54" fill="var(--yellow)"/>
    <polygon points="0,415 120,455 0,455" fill="var(--black)"/>
    <polygon points="0,428 85,455 70,455 0,432" fill="var(--yellow)"/>
    <polygon points="40,158 140,151 220,146 290,158" fill="var(--yellow)"/>
    <polygon points="40,332 290,332 220,341 140,338" fill="var(--yellow)"/>
    <g fill="none" stroke="var(--guide)" stroke-width="1" stroke-dasharray="3 2">
      <polyline points="14,14 528,14 528,113 360,113 360,357 122,357 122,442 662,442 662,14 540,14 540,126 372,126 372,369 136,369 136,430 650,430"/>
      <line x1="14" y1="14" x2="14" y2="441"/>
    </g>
  </svg>

  <div class="abs back-mark"><span class="dot"></span>Brisk Hive 360</div>
  <div class="abs vet-badge-back" role="img" aria-label="Veteran owned business membership badge"></div>

  <div class="abs inquire"><b>TEXT</b> TO INQUIRE</div>
  <ul class="abs contact-list">
    <li class="phone">
      <svg width="22" height="22" viewBox="0 0 22 22"><circle cx="11" cy="11" r="11" fill="var(--ink)"/><path d="M7 6c1-1 2 0 2.5 1.5L9 9c.5 1.5 2 3 3.5 3.5l1.5-.6c1.5.5 2.5 1.5 1.5 2.5-1 1.3-2.5 1.4-4.5.4-2-1-3.8-2.8-4.8-4.8C5.6 8 5.8 7 7 6z" fill="var(--white)"/></svg>
      (555) 014-2290
    </li>
    <li>
      <svg width="22" height="22" viewBox="0 0 22 22"><circle cx="11" cy="11" r="11" fill="var(--ink)"/><path d="M11 5a4 4 0 0 1 4 4c0 3-4 8-4 8s-4-5-4-8a4 4 0 0 1 4-4z" fill="var(--white)"/><circle cx="11" cy="9" r="1.5" fill="var(--ink)"/></svg>
      Harbor Point, Florida
    </li>
    <li>
      <svg width="22" height="22" viewBox="0 0 22 22"><circle cx="11" cy="11" r="11" fill="var(--ink)"/><rect x="5.5" y="7" width="11" height="8" fill="var(--white)"/><polyline points="5.5,7 11,11.5 16.5,7" fill="none" stroke="var(--ink)" stroke-width="1.2"/></svg>
      service@briskhive360.com
    </li>
    <li>
      <svg width="22" height="22" viewBox="0 0 22 22"><circle cx="11" cy="11" r="11" fill="var(--ink)"/><circle cx="11" cy="11" r="6" fill="none" stroke="var(--white)" stroke-width="1.3"/><ellipse cx="11" cy="11" rx="2.5" ry="6" fill="none" stroke="var(--white)" stroke-width="1.1"/><line x1="5" y1="11" x2="17" y2="11" stroke="var(--white)" stroke-width="1.1"/></svg>
      briskhive360.com
    </li>
  </ul>

  <div class="abs stamp-box"></div>
  <div class="abs address-line" style="top:229px"></div>
  <div class="abs address-line" style="top:268px"></div>
  <div class="abs address-line" style="top:307px"></div>
  <div class="abs address-line" style="top:346px"></div>
</section>

</body>
</html>
```